RTV CRAFTED

building services
decks
pergola
renovation
extensions
general building

Target Market(s)

middle to upper class

Industry/Entity Type

building

Contact Information for Business Card

my details 0427839152 pkharlow47@mailvane.net BLD574926

Font styles to use
Serif

Colors
00AB8E
00BBA5
67D7C9
C6EFE9
E9F9F6

Requirements
Must have
• logo on the front and details on the back
Nice to have
• sharp and clean lines

```html
<!DOCTYPE html>
<html lang="en">
<head>
<meta charset="utf-8">
<title>RTV CRAFTED – Business Card</title>
<link rel="stylesheet" href="https://fonts.googleapis.com/css2?family=Montserrat:wght@500;600;800&display=swap">
<style>
  :root {
    --page: #ffffff;
    --card-dark: #1c1c1c;
    --card-darker: #141414;
    --stone: #b9b9ac;
    --stone-light: #cfcfc4;
    --green: #17a674;
    --text-light: #e6e6e6;
    --divider: #d0d0d0;
  }
  * { margin: 0; padding: 0; box-sizing: border-box; }
  html, body { width: 1200px; height: 2643px; overflow: hidden; background: var(--page); }
  body { font-family: "Montserrat", sans-serif; position: relative; }

  .card {
    position: absolute; left: 390px; width: 420px; height: 735px;
    background: linear-gradient(160deg, var(--card-darker) 0%, var(--card-dark) 55%, #222 100%);
    box-shadow: 0 6px 14px rgba(0,0,0,.35);
    overflow: hidden;
  }
  .card--front { top: 546px; }
  .card--back { top: 1362px; }

  .art-area {
    position: absolute; left: 0; right: 0;
    background: linear-gradient(180deg, #151515, #1e1e1e);
  }
  .card--front .art-area { top: 0; height: 215px; border-bottom: 1px solid #262626; }
  .card--back .art-area { top: 160px; height: 250px; opacity: .6; background: linear-gradient(180deg, #202020, #1a1a1a); }

  .base-strip { position: absolute; left: 0; bottom: 0; width: 100%; height: 36px; }

  .brand {
    position: absolute; left: 0; width: 100%; text-align: center;
    color: var(--green); font-weight: 800; letter-spacing: 1px;
  }
  .card--front .brand { top: 312px; font-size: 44px; }
  .card--back .brand { top: 56px; font-size: 38px; }

  .front-url {
    position: absolute; top: 600px; width: 100%; text-align: center;
    font-size: 19px; font-weight: 600; letter-spacing: 5px; color: var(--text-light);
  }
  .front-url .accent { color: var(--green); }

  .back-head {
    position: absolute; top: 0; left: 0; width: 100%; height: 155px;
    background: linear-gradient(100deg, var(--stone) 0%, var(--stone-light) 70%, #c4c4b7 100%);
  }
  .head-rule { position: absolute; top: 151px; left: 0; width: 100%; height: 12px; }

  .holder { position: absolute; top: 188px; width: 100%; text-align: center; }
  .holder__name { color: var(--green); font-size: 28px; font-weight: 800; }
  .holder__licence { color: var(--text-light); font-size: 18px; font-weight: 500; letter-spacing: 2px; margin-top: 2px; }

  .contact { position: absolute; left: 0; width: 100%; text-align: center; color: var(--text-light); font-size: 18px; font-weight: 500; }
  .contact svg { display: block; margin: 0 auto 6px; }
  .contact--phone { top: 274px; }
  .contact--mail { top: 345px; }
  .contact--web { top: 422px; }

  .services {
    position: absolute; top: 530px; left: 40px; width: 340px;
    display: grid; grid-template-columns: 1fr 1fr; column-gap: 22px;
  }
  .services__col { display: flex; flex-direction: column; gap: 18px; }
  .services__col + .services__col { border-left: 1.5px solid var(--divider); padding-left: 22px; }
  .service { display: flex; align-items: flex-start; gap: 10px; color: var(--text-light); font-size: 16px; font-weight: 500; line-height: 1.25; letter-spacing: .5px; }
  .service__icon { flex: none; width: 18px; height: 18px; margin-top: 1px; }
</style>
</head>
<body>

<section class="card card--front">
  <div class="art-area" role="img" aria-label="Faint line drawing of a modern multi-storey building"></div>
  <div class="brand">RTV CRAFTED</div>
  <div class="front-url">www.<span class="accent">rtvcrafted</span>.com</div>
  <svg class="base-strip" viewBox="0 0 420 36" aria-hidden="true">
    <polygon points="0,22 184,22 210,2 236,22 420,22 420,36 0,36" fill="var(--stone-light)"/>
  </svg>
</section>

<section class="card card--back">
  <div class="back-head"></div>
  <div class="brand">RTV CRAFTED</div>
  <svg class="head-rule" viewBox="0 0 420 12" aria-hidden="true">
    <rect x="0" y="4" width="420" height="5" fill="var(--green)"/>
    <polygon points="200,4 210,-4 220,4" fill="var(--green)"/>
  </svg>
  <div class="art-area" role="img" aria-label="Faint line drawing of a building facade"></div>

  <div class="holder">
    <div class="holder__name">P.K HARLOW</div>
    <div class="holder__licence">BLD574926</div>
  </div>

  <div class="contact contact--phone">
    <svg width="30" height="30" viewBox="0 0 30 30" aria-hidden="true">
      <circle cx="15" cy="15" r="13" fill="none" stroke="var(--green)" stroke-width="2.5"/>
      <circle cx="15" cy="15" r="9" fill="var(--green)"/>
      <path d="M11.5 10.5c1 -.6 1.6 .6 2 1.6c.3 .8 -.8 1.2 -.6 1.8c.5 1.3 1.2 2 2.5 2.5c.6 .2 1 -.9 1.8 -.6c1 .4 2.2 1 1.6 2c-1.2 2 -5 .8 -6.8 -1.2c-2 -2 -2.6 -5.2 -.5 -6.1z" fill="#1c1c1c"/>
    </svg>
    0427839152
  </div>
  <div class="contact contact--mail">
    <svg width="30" height="30" viewBox="0 0 30 30" aria-hidden="true">
      <circle cx="15" cy="15" r="13" fill="none" stroke="var(--green)" stroke-width="2.5"/>
      <circle cx="15" cy="15" r="9" fill="var(--green)"/>
      <rect x="10" y="11.5" width="10" height="7" fill="#1c1c1c"/>
      <polyline points="10,11.5 15,15.5 20,11.5" fill="none" stroke="var(--green)" stroke-width="1.2"/>
    </svg>
    pkharlow47@mailvane.net
  </div>
  <div class="contact contact--web">
    <svg width="30" height="30" viewBox="0 0 30 30" aria-hidden="true">
      <circle cx="15" cy="15" r="13" fill="none" stroke="var(--green)" stroke-width="2.5"/>
      <circle cx="15" cy="15" r="9" fill="var(--green)"/>
      <circle cx="15" cy="15" r="5.5" fill="none" stroke="#1c1c1c" stroke-width="1.3"/>
      <ellipse cx="15" cy="15" rx="2.4" ry="5.5" fill="none" stroke="#1c1c1c" stroke-width="1.1"/>
      <line x1="9.5" y1="15" x2="20.5" y2="15" stroke="#1c1c1c" stroke-width="1.1"/>
    </svg>
    www.rtvcrafted.com
  </div>

  <div class="services">
    <div class="services__col">
      <div class="service"><svg class="service__icon" viewBox="0 0 18 18" aria-hidden="true"><rect x="2" y="6" width="14" height="10" fill="none" stroke="var(--green)" stroke-width="2"/><polygon points="1,7 9,1 17,7" fill="var(--green)"/></svg>BUILDING<br>SERVICES</div>
      <div class="service"><svg class="service__icon" viewBox="0 0 18 18" aria-hidden="true"><rect x="2" y="2" width="14" height="14" fill="var(--green)"/><line x1="6" y1="2" x2="6" y2="16" stroke="#1c1c1c" stroke-width="1.5"/><line x1="11" y1="2" x2="11" y2="16" stroke="#1c1c1c" stroke-width="1.5"/></svg>DECKS</div>
      <div class="service"><svg class="service__icon" viewBox="0 0 18 18" aria-hidden="true"><path d="M1 6 Q9 0 17 6 Z" fill="var(--green)"/><rect x="3" y="6" width="2" height="10" fill="var(--green)"/><rect x="13" y="6" width="2" height="10" fill="var(--green)"/><rect x="3" y="11" width="12" height="2" fill="var(--green)"/></svg>PERGOLA</div>
    </div>
    <div class="services__col">
      <div class="service"><svg class="service__icon" viewBox="0 0 18 18" aria-hidden="true"><circle cx="9" cy="9" r="7" fill="none" stroke="var(--green)" stroke-width="2"/><line x1="4" y1="14" x2="14" y2="4" stroke="var(--green)" stroke-width="2.5"/></svg>RENOVATION</div>
      <div class="service"><svg class="service__icon" viewBox="0 0 18 18" aria-hidden="true"><rect x="1" y="4" width="16" height="10" fill="none" stroke="var(--green)" stroke-width="2"/><line x1="6" y1="4" x2="6" y2="14" stroke="var(--green)" stroke-width="1.5"/><line x1="12" y1="4" x2="12" y2="14" stroke="var(--green)" stroke-width="1.5"/></svg>EXTENSIONS</div>
      <div class="service"><svg class="service__icon" viewBox="0 0 18 18" aria-hidden="true"><rect x="2" y="7" width="6" height="10" fill="var(--green)"/><rect x="9" y="2" width="7" height="15" fill="var(--green)"/></svg>GENERAL<br>BUILDING</div>
    </div>
  </div>

  <svg class="base-strip" viewBox="0 0 420 36" aria-hidden="true">
    <polygon points="0,22 184,22 210,2 236,22 420,22 420,36 0,36" fill="var(--stone-light)"/>
  </svg>
</section>

</body>
</html>
```